Tom Pelling Personal Website Yoga Teacher and Personal Fitness Trainer

Let's pick a WORDPRESS theme that can work with Video Bckground. I would like a website design to look like some of nice Squarespace themes.
I would like to have a Video background of me teaching. I can provide video. Please view my current Wordpress site: www.tompelling.example. I also have new logo. See file tpel1.png

Reason: I am guaranteeing this project because i believe designers can deliver. I am extending 5 days because the homepage image/video slider is intricate and takes a bit of time. I have provided details, images, video etc. in Dropbox. Tx

Target Market(s)

All people needing & wanting personal help (they can trust and feel safe and nurtured) for their health (wellness, nutrition, fitness, exercise). And people wanting extraordinary yoga teaching.

Industry/Entity Type

Fitness

Number of Pages Required

5+ page

Colors
9bcb3b
add136
cadf82
eaf2ce

Requirements
Must have
• Template that can use a video background
Nice to have
• Need to show good image gallery and testimonial videos

```html
<!DOCTYPE html>
<html lang="en">
<head>
<meta charset="utf-8">
<title>Tom Pelling — Yoga Teacher and Personal Fitness Trainer</title>
<link href="https://fonts.googleapis.com/css2?family=PT+Sans:wght@400;700&display=swap" rel="stylesheet">
<style>
  :root {
    --green: #9bcb3b;
    --green-light: #add136;
    --green-soft: #cadf82;
    --page-bg: #eaf2ce;
    --white: #ffffff;
    --ink: #4a4a4a;
    --muted: #a9a9a9;
    --footer-head: #6d9a24;
  }
  * { margin: 0; padding: 0; box-sizing: border-box; }
  html, body { width: 1200px; height: 2236px; overflow: hidden; }
  body {
    position: relative;
    background: var(--page-bg);
    font-family: "PT Sans", Arial, sans-serif;
    color: var(--ink);
  }
  .abs { position: absolute; }

  /* Header */
  .brand { left: 145px; top: 44px; display: flex; align-items: center; gap: 12px; }
  .brand-dot { width: 30px; height: 30px; border-radius: 50%; background: var(--green); }
  .brand-name { font-size: 32px; font-weight: 700; color: var(--footer-head); letter-spacing: 0.5px; }
  .search { left: 754px; top: 64px; width: 300px; height: 36px; display: flex; background: var(--white); }
  .search-field { flex: 1; display: flex; align-items: center; padding-left: 10px; gap: 10px; font-size: 10px; color: #b9b9b9; }
  .search-btn { width: 87px; background: var(--green); color: var(--white); font-size: 11px; display: flex; align-items: center; justify-content: center; }

  /* Main panel */
  .panel { left: 130px; top: 130px; width: 936px; height: 1733px; background: var(--white); box-shadow: 0 14px 24px rgba(120,140,70,0.25); }

  .nav { left: 145px; top: 145px; width: 910px; height: 58px; background: var(--green); }
  .nav-home { left: 0; top: 0; width: 79px; height: 58px; background: var(--green-light); }
  .nav-item { top: 0; height: 58px; line-height: 66px; font-size: 13px; color: var(--white); text-transform: uppercase; white-space: nowrap; }
  .nav-leaf { left: 32px; top: 8px; }

  .hero { left: 145px; top: 203px; width: 910px; height: 480px; background: linear-gradient(90deg, #2f4a1f 0%, #3d5a26 30%, #7a6a58 55%, #8a7462 75%, #4d6b2c 100%); overflow: hidden; }
  .hero-kicker { left: 31px; top: 86px; font-size: 38px; color: var(--green-soft); text-transform: uppercase; }
  .hero-title { left: 31px; top: 133px; font-size: 40px; line-height: 49px; color: var(--white); text-transform: uppercase; }
  .hero-btn { left: 31px; top: 354px; width: 116px; height: 45px; background: var(--green); color: var(--white); font-size: 15px; display: flex; align-items: center; justify-content: center; text-transform: uppercase; }
  .hero-dots { left: 31px; top: 431px; display: flex; gap: 3px; }
  .hero-dots span { width: 8px; height: 8px; border-radius: 50%; border: 1px solid var(--white); }
  .hero-dots span.active { border-color: var(--green-soft); }

  .welcome { left: 130px; top: 753px; width: 936px; text-align: center; font-size: 25px; color: var(--green); text-transform: uppercase; }
  .video { left: 222px; top: 806px; width: 756px; height: 378px; border: 5px solid var(--green-soft); background: linear-gradient(90deg, #f3a93a 0%, #f2c36a 12%, #ece6dc 28%, #f0ece6 60%, #e8e0d6 100%); overflow: hidden; }
  .video-floor { left: 0; bottom: 0; width: 100%; height: 70px; background: linear-gradient(180deg, #9c6a3d, #5a3a22); }
  .video-play { left: 323px; top: 154px; width: 88px; height: 56px; background: rgba(40,40,40,0.8); border-radius: 4px; display: flex; align-items: center; justify-content: center; }
  .video-caption { left: 0; top: 262px; width: 100%; text-align: center; font-size: 24px; color: rgba(255,255,255,0.9); }
  .video-bar { left: 57px; top: 310px; width: 632px; height: 45px; background: rgba(35,35,35,0.9); border-radius: 4px; }
  .video-track { left: 12px; top: 17px; width: 468px; height: 12px; background: #7a7a7a; border: 1px solid #222; }
  .video-progress { left: 0; top: 0; width: 132px; height: 100%; background: #1e9bd7; }
  .video-hd { left: 548px; top: 9px; font-size: 20px; font-weight: 700; font-style: italic; color: #1e9bd7; }
  .intro { left: 231px; top: 1212px; width: 738px; text-align: center; font-size: 12.5px; line-height: 20px; color: var(--muted); }

  .card { top: 1333px; height: 507px; background: var(--green); }
  .card-head { left: 0; top: 0; width: 100%; height: 73px; padding-left: 25px; line-height: 73px; font-size: 24px; color: var(--white); text-transform: uppercase; }
  .gallery { left: 145px; width: 521px; }
  .gallery-photo { left: 0; top: 73px; width: 521px; height: 308px; background: linear-gradient(110deg, #3a3a36 0%, #6d6b64 40%, #a9a59c 65%, #4e4c47 100%); }
  .arrow { top: 191px; width: 36px; height: 73px; }
  .thumb { top: 399px; width: 116px; height: 94px; }
  .testimonials { left: 690px; width: 364px; }
  .testimonial-photo { left: 0; top: 73px; width: 364px; height: 234px; background: linear-gradient(120deg, #9a9a96 0%, #c9c8c2 45%, #e0dfda 60%, #8f8e89 100%); }
  .testimonial-play { left: 160px; top: 91px; width: 50px; height: 50px; border-radius: 50%; background: rgba(255,255,255,0.75); }
  .quote-mark { left: 18px; top: 318px; font-size: 110px; font-weight: 700; color: var(--white); line-height: 1; }
  .quote-name { left: 93px; top: 341px; font-size: 19px; font-weight: 700; color: var(--white); }
  .quote-text { left: 93px; top: 368px; width: 254px; font-size: 11.5px; line-height: 19px; color: var(--white); }

  /* Footer */
  .footer-brand { left: 145px; top: 1925px; display: flex; align-items: center; gap: 9px; }
  .footer-brand .brand-dot { width: 22px; height: 22px; }
  .footer-brand .brand-name { font-size: 22px; }
  .footer-head { top: 1916px; font-size: 12px; font-weight: 700; color: var(--footer-head); }
  .footer-list { top: 1958px; list-style: none; font-size: 12px; line-height: 24px; color: var(--ink); }
  .footer-list li::before { content: "›"; margin-right: 10px; }
  .newsletter-text { left: 689px; top: 1958px; width: 365px; font-size: 11.5px; line-height: 24px; color: var(--ink); }
  .subscribe { left: 690px; top: 2008px; width: 364px; height: 35px; display: flex; background: var(--white); }
  .subscribe-field { flex: 1; display: flex; align-items: center; gap: 14px; padding-left: 8px; font-size: 10px; color: var(--green-light); }
  .subscribe-btn { width: 87px; background: var(--green); color: var(--white); font-size: 10px; display: flex; align-items: center; justify-content: center; text-transform: uppercase; }
  .bottom-rule { left: 0; top: 2191px; width: 1200px; height: 1px; background: #d6e3ad; }
  .copyright { left: 145px; top: 2206px; font-size: 11.5px; color: var(--ink); }
  .social { left: 994px; top: 2207px; display: flex; gap: 12px; }
  .social span { width: 12px; height: 12px; border-radius: 50%; background: #555; }
</style>
</head>
<body>

<header>
  <div class="abs brand"><span class="brand-dot"></span><span class="brand-name">TOM PELLING</span></div>
  <form class="abs search">
    <div class="search-field">
      <svg width="10" height="10" viewBox="0 0 10 10"><circle cx="4" cy="4" r="3" fill="none" stroke="#9bcb3b" stroke-width="1.5"/><line x1="6.3" y1="6.3" x2="9.3" y2="9.3" stroke="#9bcb3b" stroke-width="1.5"/></svg>
      Type Your Search
    </div>
    <div class="search-btn">SEARCH</div>
  </form>
</header>

<main>
  <div class="abs panel"></div>

  <nav class="abs nav">
    <div class="abs nav-home"></div>
    <svg class="abs nav-leaf" width="14" height="14" viewBox="0 0 14 14"><path d="M2 12 C2 5 7 2 12 2 C12 8 8 12 2 12 Z" fill="#ffffff"/></svg>
    <span class="abs nav-item" style="left:23px">Home</span>
    <span class="abs nav-item" style="left:96px">About</span>
    <span class="abs nav-item" style="left:175px">Blog</span>
    <span class="abs nav-item" style="left:244px">Clients</span>
    <span class="abs nav-item" style="left:328px">Contact</span>
    <span class="abs nav-item" style="left:418px">Media</span>
    <span class="abs nav-item" style="left:493px">Nutrition</span>
    <span class="abs nav-item" style="left:593px">Schedule &nbsp;/Classes</span>
    <span class="abs nav-item" style="left:752px">Servives</span>
  </nav>

  <section class="abs hero" role="img" aria-label="Portrait of Tom Pelling in a white shirt in front of green garden foliage">
    <p class="abs hero-kicker">Tom Pelling</p>
    <h1 class="abs hero-title" style="font-weight:400">I'm a Yoga<br>Teacher and<br>Personal Fitness<br>Trainer</h1>
    <a class="abs hero-btn">Learn More+</a>
    <div class="abs hero-dots"><span class="active"></span><span></span><span></span><span></span></div>
  </section>

  <h2 class="abs welcome" style="font-weight:400">Welcome to Yoga Teaching</h2>

  <div class="abs video">
    <div class="abs" role="img" aria-label="Video still of a yoga teacher in a triangle pose in a bright studio with curtains" style="inset:0">
      <div class="abs video-floor"></div>
    </div>
    <div class="abs video-play">
      <svg width="20" height="22" viewBox="0 0 20 22"><path d="M2 1 L19 11 L2 21 Z" fill="#ffffff"/></svg>
    </div>
    <p class="abs video-caption">I'm a Yoga Teacher and Personal Fitness Trainer</p>
    <div class="abs video-bar">
      <div class="abs video-track"><div class="abs video-progress"></div></div>
      <svg class="abs" style="left:490px;top:13px" width="46" height="20" viewBox="0 0 46 20">
        <rect x="0" y="2" width="4" height="16" fill="#1e9bd7"/><rect x="7" y="2" width="4" height="16" fill="#1e9bd7"/><rect x="14" y="2" width="4" height="16" fill="#1e9bd7"/><rect x="21" y="2" width="4" height="16" fill="#1e9bd7"/><rect x="28" y="2" width="4" height="16" fill="#1e9bd7"/><rect x="35" y="2" width="4" height="16" fill="#1e9bd7"/>
      </svg>
      <span class="abs video-hd">HD</span>
      <svg class="abs" style="left:596px;top:13px" width="18" height="18" viewBox="0 0 18 18" fill="#ffffff">
        <path d="M1 1 L7 1 L1 7 Z M17 1 L17 7 L11 1 Z M1 17 L1 11 L7 17 Z M17 17 L11 17 L17 11 Z"/>
      </svg>
    </div>
  </div>

  <p class="abs intro">Lorem Ipsum is simply dummy text of the printing and typesetting industry. Lorem Ipsum has been the industry's standard dummy text ever since the 1500s, when an unknown printer took a galley of type and scrambled it to make a type specimen book. It has survived not only five centuries, but also the leap into electronic typesetting</p>

  <section class="abs card gallery">
    <h3 class="abs card-head" style="font-weight:400">Photo Gallery</h3>
    <div class="abs gallery-photo" role="img" aria-label="Black and white photo of the teacher reaching toward a large tree trunk"></div>
    <svg class="abs arrow" style="left:0" viewBox="0 0 36 73"><path d="M0 0 A36 36.5 0 0 1 0 73 Z" fill="#9bcb3b"/><path d="M10 28 L18 36.5 L10 45" fill="none" stroke="#ffffff" stroke-width="3"/></svg>
    <svg class="abs arrow" style="left:485px" viewBox="0 0 36 73"><path d="M36 0 A36 36.5 0 0 0 36 73 Z" fill="#9bcb3b"/><path d="M26 28 L18 36.5 L26 45" fill="none" stroke="#ffffff" stroke-width="3"/></svg>
    <div class="abs thumb" style="left:19px;background:linear-gradient(135deg,#1f3a1a,#3f6a2c)" role="img" aria-label="Thumbnail of an outdoor yoga class at night"></div>
    <div class="abs thumb" style="left:141px;background:linear-gradient(135deg,#b8744a,#e0a070)" role="img" aria-label="Thumbnail of students in a studio class"></div>
    <div class="abs thumb" style="left:263px;background:linear-gradient(135deg,#c9a07a,#8a5a3a)" role="img" aria-label="Thumbnail of a group practising poses"></div>
    <div class="abs thumb" style="left:386px;background:linear-gradient(135deg,#2e4a22,#8a6a52)" role="img" aria-label="Thumbnail of a teacher assisting a student outdoors"></div>
  </section>

  <section class="abs card testimonials">
    <h3 class="abs card-head" style="font-weight:400">Testimonials</h3>
    <div class="abs testimonial-photo" role="img" aria-label="Black and white video still of two people seated on the floor in a workshop">
      <div class="abs testimonial-play"></div>
      <svg class="abs" style="left:179px;top:106px" width="16" height="20" viewBox="0 0 16 20"><path d="M1 1 L15 10 L1 19 Z" fill="#ffffff"/></svg>
    </div>
    <span class="abs quote-mark">“</span>
    <h4 class="abs quote-name">Nella Brooke</h4>
    <p class="abs quote-text">Lorem Ipsum is simply dummy text of the printing and typesetting industry. Lorem Ipsum has been the industry's standard dummy text ever since the 1500s, when an unknown printer took a galley of type and scrambled</p>
  </section>
</main>

<footer>
  <div class="abs footer-brand"><span class="brand-dot"></span><span class="brand-name">TOM PELLING</span></div>

  <h5 class="abs footer-head" style="left:377px">Menu Links</h5>
  <ul class="abs footer-list" style="left:377px">
    <li>Home</li><li>About</li><li>Blog</li><li>Clients</li><li>Contact</li><li>Media</li><li>Nutrition</li><li>Schedule &nbsp;/Classes</li><li>Servives</li>
  </ul>

  <h5 class="abs footer-head" style="left:534px">Other Links</h5>
  <ul class="abs footer-list" style="left:534px">
    <li>Terms Of Conditions</li><li>Privacy Policy</li>
  </ul>

  <h5 class="abs footer-head" style="left:689px">Newsletter Sign Up</h5>
  <p class="abs newsletter-text">Lorem Ipsum is simply dummy text of the printing and typesetting industry. Lorem Ipsum has been the industry's</p>
  <form class="abs subscribe">
    <div class="subscribe-field">
      <svg width="14" height="10" viewBox="0 0 14 10"><rect x="0.5" y="0.5" width="13" height="9" fill="none" stroke="#9bcb3b"/><path d="M0.5 0.5 L7 6 L13.5 0.5" fill="none" stroke="#9bcb3b"/></svg>
      Enter your E-mail Address
    </div>
    <div class="subscribe-btn">Subscribe</div>
  </form>

  <div class="abs bottom-rule"></div>
  <p class="abs copyright">© 2015 Company Name | All Rights Reserved</p>
  <div class="abs social" aria-label="Social links"><span></span><span></span><span></span></div>
</footer>

</body>
</html>
```